4th Generation Family Business Needs a New Card Design!

We are a family owned 4th Generation company. We are based in the Sydney, Australia area and we are desperately in need of a more modern and classy card. We are monumental masons who design, supply & erect lasting memorials throughout cemeteries in Sydney. Our customers are normally in a period of grieving. I have attached logo files that will need to be implemented on the card. Company was established 1935. Australian Owned and Operated. Card needs to be designed to PRINTLY.com specification.

Target Market(s)

Our target market is based upon people that a grieving for family members that have passed away. We also deal with alot of companies that own and operate cemeteries.

Industry/Entity Type

Business

Contact Information for Business Card

Oliver Brantley, Operations Manager, 0417552908, oliver@hollowaystoneworks.com.au
Martin Brantley, Director, 0431906627, martin@hollowaystoneworks.com.au
Phone # 02 9634 2258
Website: www.hollowaystoneworks.com.au
Address: Suite 17, 8 Calloway Lane, East Penrose, Sydney NSW 2290

Font styles to use
Serif
Decorative
Script

Requirements
Must have
• Would like to see the logo nicely implemented with a modern design. Embossed lettering would be a nice additive.

```html
<!DOCTYPE html>
<html lang="en">
<head>
<meta charset="utf-8">
<title>Holloway Stoneworks – Business Cards</title>
<link rel="stylesheet" href="https://fonts.googleapis.com/css2?family=Cinzel:wght@400;600;700&family=Cormorant+Garamond:ital,wght@1,500&display=swap">
<style>
  :root {
    --backdrop: #1c1d1f;
    --stone-light: #9fb0b2;
    --stone-mid: #8a9c9f;
    --stone-edge: #6f8184;
    --slate-dark: #2e302c;
    --slate-deep: #1f211e;
    --ink: #2a2d2c;
    --ink-soft: #3a3f3f;
    --paper: #f1f1ec;
  }
  * { box-sizing: border-box; margin: 0; padding: 0; }
  html, body { width: 1200px; height: 907px; overflow: hidden; }
  body { background: var(--backdrop); position: relative; font-family: "Cinzel", serif; }

  .card {
    position: absolute;
    width: 570px;
    height: 360px;
    border-radius: 10px;
    overflow: hidden;
    box-shadow: 0 8px 22px rgba(0,0,0,.6);
  }
  .card--nathan { left: 20px;  top: 60px; }
  .card--back-a { left: 610px; top: 60px; }
  .card--back-b { left: 20px;  top: 487px; }
  .card--martin { left: 610px; top: 487px; }

  .stone {
    position: absolute; inset: 0;
    background:
      radial-gradient(ellipse at 30% 25%, rgba(255,255,255,.14), transparent 60%),
      radial-gradient(ellipse at 80% 85%, rgba(40,50,50,.25), transparent 60%),
      linear-gradient(160deg, var(--stone-light), var(--stone-mid) 60%, var(--stone-edge));
  }

  /* front */
  .identity {
    position: absolute; left: 0; top: 0; width: 260px; height: 100%;
    display: flex; flex-direction: column; align-items: center; text-align: center;
    color: var(--ink);
  }
  .wordmark {
    margin-top: 60px;
    display: flex; flex-direction: column; align-items: center; gap: 10px;
    font-weight: 700; font-size: 24px; line-height: 1.05; letter-spacing: .5px;
    color: var(--ink);
  }
  .wordmark__mark { width: 22px; height: 22px; background: var(--ink); }
  .person { margin-top: 56px; }
  .person__name { font-size: 19px; font-weight: 600; letter-spacing: .5px; }
  .person__role { font-size: 12px; font-weight: 600; margin-top: 2px; }
  .established {
    position: absolute; bottom: 24px; left: 0; width: 100%;
    font-family: "Cormorant Garamond", serif; font-style: italic; font-weight: 500;
    font-size: 22px; color: var(--ink-soft);
  }

  .contact-panel {
    position: absolute; left: 248px; top: 0; width: 322px; height: 100%;
    background:
      radial-gradient(ellipse at 70% 20%, rgba(255,255,255,.06), transparent 60%),
      linear-gradient(170deg, var(--slate-dark), var(--slate-deep));
    clip-path: polygon(12px 0, 100% 0, 100% 100%, 12px 100%, 12px 51%, 0 46%, 12px 41%);
    padding: 22px 14px 22px 34px;
    display: flex; flex-direction: column; justify-content: space-between;
  }
  .contact {
    display: flex; align-items: center; gap: 12px;
    color: var(--paper); font-size: 11.5px; letter-spacing: .3px; line-height: 1.5;
  }
  .contact__icon {
    flex: none; width: 28px; height: 28px; border-radius: 50%;
    background: var(--paper); display: grid; place-items: center;
  }
  .contact__icon svg { width: 16px; height: 16px; fill: var(--slate-deep); stroke: var(--slate-deep); }

  /* back */
  .back-name {
    position: absolute; inset: 0;
    display: flex; flex-direction: column; align-items: center; justify-content: center; gap: 18px;
    color: #3d4546; font-weight: 700; text-align: center;
  }
  .back-name__mark { width: 48px; height: 48px; background: #3d4546; }
  .back-name__text { font-size: 46px; line-height: 1.1; letter-spacing: 1px; }
</style>
</head>
<body>

<svg width="0" height="0" style="position:absolute" aria-hidden="true">
  <defs>
    <symbol id="icon-web" viewBox="0 0 16 16"><circle cx="8" cy="8" r="6.5" fill="none" stroke-width="1.4"/><path d="M1.5 8h13M8 1.5c-2.5 3-2.5 10 0 13M8 1.5c2.5 3 2.5 10 0 13" fill="none" stroke-width="1.2"/></symbol>
    <symbol id="icon-mobile" viewBox="0 0 16 16"><rect x="4" y="1" width="8" height="14" rx="1.5" fill="none" stroke-width="1.5"/><circle cx="8" cy="12.5" r=".9" stroke="none"/></symbol>
    <symbol id="icon-phone" viewBox="0 0 16 16"><path stroke="none" d="M3.6 1.5l2.3 2.6-1.4 1.8c.9 2 2.4 3.5 4.4 4.4l1.8-1.4 2.6 2.3-1.4 2.3C7 13.6 2.4 9 1.5 3.5z"/></symbol>
    <symbol id="icon-mail" viewBox="0 0 16 16"><rect x="1.5" y="3.5" width="13" height="9" fill="none" stroke-width="1.4"/><path d="M1.5 3.5L8 9l6.5-5.5" fill="none" stroke-width="1.3"/></symbol>
    <symbol id="icon-pin" viewBox="0 0 16 16"><path stroke="none" d="M8 1a5 5 0 0 0-5 5c0 3.6 5 9 5 9s5-5.4 5-9a5 5 0 0 0-5-5zm0 7a2 2 0 1 1 0-4 2 2 0 0 1 0 4z"/></symbol>
  </defs>
</svg>

<article class="card card--nathan">
  <div class="stone" role="img" aria-label="Grey weathered stone texture"></div>
  <div class="identity">
    <div class="wordmark"><span class="wordmark__mark"></span>Holloway<br>Stoneworks</div>
    <div class="person">
      <p class="person__name">Oliver Brantley</p>
      <p class="person__role">Operations Manager</p>
    </div>
    <p class="established">Est. 1935</p>
  </div>
  <ul class="contact-panel">
    <li class="contact"><span class="contact__icon"><svg><use href="#icon-web"/></svg></span>www.hollowaystoneworks.com.au</li>
    <li class="contact"><span class="contact__icon"><svg><use href="#icon-mobile"/></svg></span>+04 1755 2908</li>
    <li class="contact"><span class="contact__icon"><svg><use href="#icon-phone"/></svg></span>+02 9634 2258</li>
    <li class="contact"><span class="contact__icon"><svg><use href="#icon-mail"/></svg></span>oliver@hollowaystoneworks.com.au</li>
    <li class="contact"><span class="contact__icon"><svg><use href="#icon-pin"/></svg></span><span>Suite 17, 8 Calloway Lane,<br>East Penrose, Sydney NSW 2290</span></li>
  </ul>
</article>

<article class="card card--back-a">
  <div class="stone" role="img" aria-label="Grey weathered stone texture"></div>
  <div class="back-name"><span class="back-name__mark"></span><p class="back-name__text">Holloway<br>Stoneworks</p></div>
</article>

<article class="card card--back-b">
  <div class="stone" role="img" aria-label="Grey weathered stone texture"></div>
  <div class="back-name"><span class="back-name__mark"></span><p class="back-name__text">Holloway<br>Stoneworks</p></div>
</article>

<article class="card card--martin">
  <div class="stone" role="img" aria-label="Grey weathered stone texture"></div>
  <div class="identity">
    <div class="wordmark"><span class="wordmark__mark"></span>Holloway<br>Stoneworks</div>
    <div class="person">
      <p class="person__name">Martin Brantley</p>
      <p class="person__role">Director</p>
    </div>
    <p class="established">Est. 1935</p>
  </div>
  <ul class="contact-panel">
    <li class="contact"><span class="contact__icon"><svg><use href="#icon-web"/></svg></span>www.hollowaystoneworks.com.au</li>
    <li class="contact"><span class="contact__icon"><svg><use href="#icon-mobile"/></svg></span>+04 3190 6627</li>
    <li class="contact"><span class="contact__icon"><svg><use href="#icon-phone"/></svg></span>+02 9634 2258</li>
    <li class="contact"><span class="contact__icon"><svg><use href="#icon-mail"/></svg></span>martin@hollowaystoneworks.com.au</li>
    <li class="contact"><span class="contact__icon"><svg><use href="#icon-pin"/></svg></span><span>Suite 17, 8 Calloway Lane,<br>East Penrose, Sydney NSW 2290</span></li>
  </ul>
</article>

</body>
</html>
```